I want a business letter head designed, one that I can have printed but also one that I can use as an insert for proforma documentation that is printed in house.

Business name : RJ Penfold & Associates
Address: PO Box 738
Tewantin Qld 4587

Type of business: Accounting practice- accounting, taxation, audit, self managed superannuation,

Colour scheme: black and blue - previously designed a business card; however the blue that is one the cards is very washed out and I am not particularly happy with it.

Industry/Entity Type

Business

```html
<!DOCTYPE html>
<html lang="en">
<head>
<meta charset="utf-8">
<title>RJ Penfold &amp; Associates — Letterhead</title>
<link rel="stylesheet" href="https://fonts.googleapis.com/css2?family=Libre+Baskerville:wght@700&family=Open+Sans:wght@600&display=swap">
<style>
  :root {
    --backdrop: #e9e9e9;
    --paper: #ffffff;
    --ink: #141414;
    --band: #000000;
    --brand-blue: #5f8ac4;
    --address-blue: #7ea3d6;
  }
  * { box-sizing: border-box; margin: 0; padding: 0; }
  html, body {
    width: 1200px;
    height: 943px;
    overflow: hidden;
    background: var(--backdrop);
  }
  .letterhead {
    position: absolute;
    top: 18px;
    left: 280px;
    width: 640px;
    height: 906px;
    background: var(--paper);
    box-shadow: 0 2px 10px rgba(0,0,0,0.12);
    overflow: hidden;
  }
  .side-band {
    position: absolute;
    top: 0;
    left: 0;
    width: 60px;
    height: 100%;
    background: var(--band);
  }
  .side-rule {
    position: absolute;
    top: 0;
    left: 60px;
    width: 6px;
    height: 100%;
    background: var(--brand-blue);
  }
  .postal-address {
    position: absolute;
    left: 0;
    bottom: 40px;
    width: 60px;
    display: flex;
    justify-content: center;
    writing-mode: vertical-rl;
    transform: rotate(180deg);
    font-family: "Open Sans", sans-serif;
    font-weight: 600;
    font-size: 15px;
    letter-spacing: 0.3px;
    color: var(--address-blue);
    white-space: nowrap;
  }
  .postal-address .divider { padding: 6px 0; }
  .business-name {
    position: absolute;
    top: 58px;
    left: 96px;
    font-family: "Libre Baskerville", serif;
    font-weight: 700;
    font-size: 18px;
    line-height: 1.2;
    color: var(--ink);
    white-space: nowrap;
  }
</style>
</head>
<body>
  <main class="letterhead">
    <div class="side-band"></div>
    <div class="side-rule"></div>
    <p class="postal-address">PO Box 738<span class="divider">|</span>Tewantin Qld 4587</p>
    <h1 class="business-name">RJ Penfold &amp; Associates</h1>
  </main>
</body>
</html>
```